Professional Modern Website Design

We are a premium IT services provider to the financial industry based in London. Our company is called Veltra our current holding page is www.veltra-example.co.uk. We require a new website to match our new corporate identity. This project is for the design phase only. Development will be handled in-house. I have attached examples of wire frames we have developed (although open to suggestions for improvement) Our brand document that should demonstrate current brand, inc how we communicate to potential clients and finally mostly completed web-content.
We are looking for designers that can create something that sets us apart from our competitors.
Target Market(s)
IT Decision makers in Finance companies such as; hedge funds, private investment banks etc
Industry/Entity Type
Financial
Number of Pages Required
5+ page
Requirements
Must have
- hexagon elements in the design, unique design.
Nice to have
- Blog and social media feeds
Should not have
- Should not resemble a downloaded template

```html
<!DOCTYPE html>
<html lang="en">
<head>
<meta charset="utf-8">
<title>Veltra – IT Services for the Finance Industry</title>
<link rel="stylesheet" href="https://fonts.googleapis.com/css2?family=Lato:wght@300;400;700;900&display=swap">
<style>
:root{
  --orange:#f05a1a;
  --orange-dark:#d94c10;
  --ink:#2b2b2b;
  --text:#555;
  --muted:#8a8a8a;
  --line:#d9d9d9;
  --slate:#3c4757;
  --slate-dark:#262f3b;
  --yellow:#f5b400;
  --black:#111;
  --footer:#141414;
  --white:#fff;
  --hero-a:#eef1f5;
  --hero-b:#c9d0da;
  --hex-grey:#d5d5d5;
}
*{box-sizing:border-box;margin:0;padding:0}
html,body{width:1200px;height:3293px;overflow:hidden}
body{font-family:'Lato',Arial,sans-serif;color:var(--text);background:var(--white);position:relative}
.abs{position:absolute}
.center{text-align:center;left:0;width:1200px}

/* header */
.site-header{top:0;left:0;width:1200px;height:148px;background:var(--white)}
.brand{left:172px;top:18px;width:90px;text-align:center}
.brand-mark{width:70px;height:70px;background:var(--orange);margin:0 auto}
.brand-name{font-size:15px;letter-spacing:5px;color:var(--muted);margin-top:12px;font-weight:400}
.topbar{right:170px;top:30px;font-size:13px;color:var(--muted)}
.topbar strong{color:var(--ink);margin-left:18px;font-weight:700}
.topbar .search{display:inline-block;width:11px;height:11px;border:2px solid var(--muted);border-radius:50%;margin-left:18px;vertical-align:middle}
.main-nav{right:170px;top:82px;display:flex;align-items:center;gap:26px;font-size:13px;letter-spacing:1px;color:var(--text)}
.main-nav .caret{font-size:9px;margin-left:4px}
.btn-login{border:1px solid var(--ink);padding:8px 16px;color:var(--ink);font-weight:700}
.main-nav .register{color:var(--muted)}

/* hero */
.hero{top:148px;left:0;width:1200px;height:512px;background:linear-gradient(100deg,var(--hero-a) 0%,#e2e7ee 45%,var(--hero-b) 100%)}
.hero-copy{left:176px;top:100px;width:330px;text-align:center}
.hero-kicker{font-size:15px;letter-spacing:5px;color:var(--ink)}
.hero-lead{font-size:19px;letter-spacing:2px;color:var(--ink);margin-top:8px;font-weight:700}
.hero-box{background:var(--white);margin-top:12px;height:54px;line-height:54px;font-size:40px;font-weight:300;letter-spacing:3px;color:#9aa7b8;text-transform:uppercase}
.hero-small{font-size:13px;color:var(--text);margin-top:22px}
.hero-industry{font-size:14px;letter-spacing:4px;color:var(--ink);margin-top:6px}
.hero-link{display:inline-block;margin-top:42px;font-size:14px;font-weight:700;color:var(--ink);border-bottom:2px solid var(--ink);padding-bottom:2px}

.exp-badge{left:520px;top:574px;width:160px;height:176px}
.exp-label{top:752px;font-size:14px;letter-spacing:6px;color:var(--ink);font-weight:700}

/* section headings */
.rule{left:270px;width:660px;height:1px;background:var(--line)}
.kicker{font-size:12px;letter-spacing:5px;color:var(--muted)}
.section-title{font-size:26px;letter-spacing:6px;color:var(--ink);font-weight:400;text-transform:uppercase}
.section-sub{font-size:22px;font-weight:300;color:var(--ink)}
.section-text{left:220px;width:760px;text-align:center;font-size:13px;line-height:21px;color:var(--text)}

/* values */
.value{width:260px;text-align:center}
.value svg{display:block;margin:0 auto}
.value-desc{font-size:13px;line-height:20px;color:var(--text);margin-top:14px;padding:0 30px}
.btn-orange{left:505px;top:1445px;width:190px;height:38px;background:var(--orange);color:var(--white);font-size:12px;letter-spacing:2px;font-weight:700;text-align:center;line-height:38px}

/* people */
.people{top:1537px;left:0;width:1200px;height:549px;background:linear-gradient(90deg,var(--slate-dark),var(--slate) 50%,#4d5a6b)}
.people .kicker{color:#cfd5dd}
.people .section-title{color:var(--white)}
.people .section-sub{color:#e6e9ee}
.portrait{left:495px;top:178px;width:210px;height:210px;border-radius:50%;background:radial-gradient(circle at 50% 40%,#e9d6c8,#a8b3c2 75%);border:5px solid var(--white)}
.btn-live{left:545px;top:398px;width:110px;height:28px;background:var(--yellow);color:var(--ink);font-size:11px;letter-spacing:1px;text-align:center;line-height:28px;font-weight:700}
.people-role{top:446px;font-size:12px;letter-spacing:2px;color:var(--white)}
.people-text{left:330px;width:540px;top:474px;text-align:center;font-size:12px;line-height:19px;color:#c6ccd5}
.slider-arrow{top:262px}

/* services */
.services{top:2086px;left:0;width:1200px;height:294px;background:var(--orange)}
.services .kicker{color:#ffd8c6}
.services .section-title{color:var(--white)}
.services-list{top:132px;font-size:17px;line-height:34px;color:var(--white)}
.services-more{top:230px;font-size:13px;font-weight:700;color:var(--white);letter-spacing:1px}
.services-more span{border-bottom:2px solid var(--white);padding-bottom:2px}

/* awards */
.award{width:160px;height:176px}

/* footer */
.site-footer{top:2873px;left:0;width:1200px;height:420px;background:var(--footer);color:#9a9a9a}
.foot-head{font-size:13px;font-weight:700;letter-spacing:1px;color:var(--orange);text-transform:uppercase}
.foot-list{list-style:none;font-size:13px;line-height:32px;margin-top:18px}
.foot-text{font-size:13px;line-height:22px}
.foot-tel{font-size:24px;color:var(--white);font-weight:400}
.foot-tel small{font-size:13px;color:#9a9a9a;margin-right:6px}
.social{display:flex;gap:6px;margin-top:18px}
.social span{width:30px;height:30px;background:#3a3a3a}
.blog-date{width:30px;height:44px;background:var(--orange);color:var(--white);font-size:11px;text-align:center;line-height:14px;padding-top:8px;font-weight:700}
.blog-img{width:92px;height:110px;background:linear-gradient(160deg,#5a6b85,#2d3848)}
.foot-brand{left:860px;top:70px}
.foot-brand .brand-mark{width:62px;height:62px;margin:0}
.foot-brand .brand-name{text-align:left;margin-top:10px;color:#9a9a9a}
</style>
</head>
<body>

<header class="site-header abs">
  <div class="brand abs">
    <div class="brand-mark"></div>
    <div class="brand-name">VELTRA</div>
  </div>
  <div class="topbar abs">Email: info@veltra-example.co.uk <strong>CALL: +44 20 7946 0182</strong><span class="search"></span></div>
  <nav class="main-nav abs">
    <span>ABOUT</span>
    <span>SERVICES<span class="caret">▼</span></span>
    <span>PARTNERS</span>
    <span>CLIENTS</span>
    <span>CONTACT</span>
    <span class="btn-login">LOGIN</span>
    <span class="register">REGISTER</span>
  </nav>
</header>

<section class="hero abs" role="img" aria-label="Photograph of a smiling consultant in shirt and tie pointing at the headline, in a bright office">
  <div class="hero-copy abs">
    <div class="hero-kicker">VELTRA</div>
    <div class="hero-lead">PROVIDING EXPERT</div>
    <div class="hero-box">IT Service</div>
    <div class="hero-box">Support</div>
    <div class="hero-small">to the finance</div>
    <div class="hero-industry">FINANCE INDUSTRY</div>
    <div class="hero-link">Explore More</div>
  </div>
</section>

<svg class="exp-badge abs" viewBox="0 0 160 176" aria-label="More than 40 years">
  <polygon points="80,2 158,46 158,130 80,174 2,130 2,46" fill="#111" stroke="#fff" stroke-width="3"/>
  <text x="80" y="52" text-anchor="middle" font-family="Lato,Arial,sans-serif" font-size="10" fill="#fff" letter-spacing="1">WE HAVE</text>
  <text x="80" y="72" text-anchor="middle" font-family="Lato,Arial,sans-serif" font-size="14" fill="#fff">more than</text>
  <text x="80" y="122" text-anchor="middle" font-family="Lato,Arial,sans-serif" font-size="54" font-weight="300" fill="#f05a1a">40</text>
  <text x="80" y="142" text-anchor="middle" font-family="Lato,Arial,sans-serif" font-size="10" fill="#fff" letter-spacing="1">YEARS</text>
</svg>
<div class="exp-label abs center">EXPERIENCE</div>

<div class="rule abs" style="top:795px"></div>

<!-- brand values -->
<div class="kicker abs center" style="top:826px">VELTRA'S</div>
<h2 class="section-title abs center" style="top:850px">Brand Values</h2>
<p class="section-sub abs center" style="top:902px">Expert provider of IT services &amp; support</p>
<p class="section-text abs" style="top:966px">Veltra is an expert provider of IT services and support to the financial industry throughout London and the world's top financial hubs. We have over 12 years' experience supporting finance technology and pride ourselves on...</p>

<div class="value abs" style="left:163px;top:1052px">
  <svg width="250" height="276" viewBox="0 0 250 276">
    <polygon points="125,3 247,72 247,204 125,273 3,204 3,72" fill="none" stroke="#cfcfcf" stroke-width="2"/>
    <text x="125" y="62" text-anchor="middle" font-family="Lato,Arial,sans-serif" font-size="11" letter-spacing="3" fill="#8a8a8a">OUR</text>
    <text x="125" y="90" text-anchor="middle" font-family="Lato,Arial,sans-serif" font-size="21" letter-spacing="3" fill="#2b2b2b">COMMITMENT</text>
    <rect x="85" y="118" width="80" height="64" rx="6" fill="#b5b5b5" role="img" aria-label="Handshake icon"/>
    <rect x="100" y="240" width="50" height="16" fill="#111"/>
    <text x="125" y="252" text-anchor="middle" font-family="Lato,Arial,sans-serif" font-size="8" fill="#fff" letter-spacing="1">VALUE 01</text>
  </svg>
  <p class="value-desc">Our core skills derive from IT management and delivering high value technology solutions through excellent knowledge</p>
</div>

<div class="value abs" style="left:470px;top:1052px">
  <svg width="250" height="276" viewBox="0 0 250 276">
    <polygon points="125,3 247,72 247,204 125,273 3,204 3,72" fill="none" stroke="#cfcfcf" stroke-width="2"/>
    <text x="125" y="62" text-anchor="middle" font-family="Lato,Arial,sans-serif" font-size="11" letter-spacing="3" fill="#8a8a8a">OUR</text>
    <text x="125" y="90" text-anchor="middle" font-family="Lato,Arial,sans-serif" font-size="21" letter-spacing="3" fill="#2b2b2b">DYNAMISM</text>
    <path d="M97 150 A28 28 0 0 1 148 134" fill="none" stroke="#b5b5b5" stroke-width="7"/>
    <polygon points="140,122 160,130 146,146" fill="#b5b5b5"/>
    <path d="M153 150 A28 28 0 0 1 102 166" fill="none" stroke="#b5b5b5" stroke-width="7"/>
    <polygon points="110,178 90,170 104,154" fill="#b5b5b5"/>
    <rect x="100" y="240" width="50" height="16" fill="#111"/>
    <text x="125" y="252" text-anchor="middle" font-family="Lato,Arial,sans-serif" font-size="8" fill="#fff" letter-spacing="1">VALUE 02</text>
  </svg>
  <p class="value-desc">Our core skills derive from IT management and delivering high value technology solutions through excellent knowledge</p>
</div>

<div class="value abs" style="left:777px;top:1052px">
  <svg width="250" height="276" viewBox="0 0 250 276">
    <polygon points="125,3 247,72 247,204 125,273 3,204 3,72" fill="none" stroke="#cfcfcf" stroke-width="2"/>
    <text x="125" y="62" text-anchor="middle" font-family="Lato,Arial,sans-serif" font-size="11" letter-spacing="3" fill="#8a8a8a">OUR</text>
    <text x="125" y="90" text-anchor="middle" font-family="Lato,Arial,sans-serif" font-size="21" letter-spacing="3" fill="#2b2b2b">AGILITY</text>
    <rect x="86" y="124" width="8" height="52" fill="#b5b5b5"/>
    <polygon points="100,124 128,150 100,176" fill="#b5b5b5"/>
    <polygon points="130,124 158,150 130,176" fill="#b5b5b5"/>
    <rect x="100" y="240" width="50" height="16" fill="#111"/>
    <text x="125" y="252" text-anchor="middle" font-family="Lato,Arial,sans-serif" font-size="8" fill="#fff" letter-spacing="1">VALUE 03</text>
  </svg>
  <p class="value-desc">Our core skills derive from IT management and delivering high value technology solutions through excellent knowledge</p>
</div>

<div class="btn-orange abs">READ MORE &nbsp;→</div>

<!-- people -->
<section class="people abs" role="img" aria-label="Dimmed photograph of colleagues working in an office">
  <div class="kicker abs center" style="top:64px">VELTRA'S</div>
  <h2 class="section-title abs center" style="top:86px">Our People</h2>
  <p class="section-sub abs center" style="top:132px">Morbi vel dolor eulit congue bibendum</p>
  <svg class="slider-arrow abs" style="left:76px" width="16" height="30" viewBox="0 0 16 30"><polyline points="14,2 2,15 14,28" fill="none" stroke="#fff" stroke-width="2"/></svg>
  <svg class="slider-arrow abs" style="left:1108px" width="16" height="30" viewBox="0 0 16 30"><polyline points="2,2 14,15 2,28" fill="none" stroke="#fff" stroke-width="2"/></svg>
  <div class="portrait abs" role="img" aria-label="Portrait of a support team member wearing a headset"></div>
  <div class="btn-live abs">SPEAK LIVE</div>
  <div class="people-role abs center">IT SUPPORT</div>
  <p class="people-text abs">Pellentesque vitae dolor cursus ullamcorper erat, quis tempus eros with dapibus laoreet lacinia, metus massa mattis quis purus mise enim.</p>
</section>

<!-- services -->
<section class="services abs">
  <div class="kicker abs center" style="top:44px">VELTRA'S</div>
  <h2 class="section-title abs center" style="top:66px">Services Include</h2>
  <p class="services-list abs center">Technical Support, It Management &amp; Consultancy And Information Security<br>And Risk Management</p>
  <div class="services-more abs center"><span>MORE</span></div>
</section>

<!-- awards -->
<div class="kicker abs center" style="top:2450px">VELTRA'S</div>
<h2 class="section-title abs center" style="top:2474px">Awards</h2>
<p class="section-sub abs center" style="top:2524px">Expert provider of IT services &amp; support</p>
<p class="section-text abs" style="top:2572px">Veltra is an expert provider of IT services and support to the financial industry throughout London and the world's top financial hubs. We have over 12 years' experience supporting finance technology and pride ourselves on...</p>

<svg class="award abs" style="left:176px;top:2650px" viewBox="0 0 160 176" aria-label="Award badge"><polygon points="80,2 158,46 158,130 80,174 2,130 2,46" fill="#d5d5d5"/></svg>
<svg class="award abs" style="left:418px;top:2650px" viewBox="0 0 160 176" aria-label="Award badge"><polygon points="80,2 158,46 158,130 80,174 2,130 2,46" fill="#d5d5d5"/></svg>
<svg class="award abs" style="left:652px;top:2650px" viewBox="0 0 160 176" aria-label="Award badge"><polygon points="80,2 158,46 158,130 80,174 2,130 2,46" fill="#d5d5d5"/></svg>
<svg class="award abs" style="left:893px;top:2650px" viewBox="0 0 160 176" aria-label="Award badge"><polygon points="80,2 158,46 158,130 80,174 2,130 2,46" fill="#d5d5d5"/></svg>

<!-- footer -->
<footer class="site-footer abs">
  <div class="abs" style="left:172px;top:68px">
    <div class="foot-head">Sitemap</div>
    <ul class="foot-list">
      <li>About</li><li>Services</li><li>Partners</li><li>Clients</li><li>Contact</li>
    </ul>
  </div>
  <div class="abs" style="left:322px;top:68px;width:230px">
    <div class="foot-head">London Office</div>
    <p class="foot-text" style="margin-top:18px">18 Harbour Lane, Finsbury<br>London EC2 4RT</p>
    <p class="foot-text" style="margin-top:16px">Email: info@veltra-example.co.uk</p>
    <p class="foot-tel" style="margin-top:16px"><small>Tel:</small>+44 20 7946 0182</p>
    <div class="social"><span></span><span></span><span></span><span></span></div>
  </div>
  <div class="abs" style="left:585px;top:68px;width:200px">
    <div class="foot-head">Blog</div>
    <div class="blog-date abs" style="top:34px;left:0">12<br>MAY</div>
    <p class="foot-text abs" style="top:34px;left:42px;width:150px;line-height:18px;color:#ccc">Individual stil, do observe</p>
    <div class="blog-img abs" style="top:86px;left:42px" role="img" aria-label="Blog post photograph"></div>
    <p class="foot-text abs" style="top:204px;left:42px;width:150px;line-height:18px;font-size:12px">Posted by <span style="color:var(--orange)">Maren Holt</span><br>Secure cloud services for private banking teams and funds.</p>
  </div>
  <div class="foot-brand abs">
    <div class="brand-mark"></div>
    <div class="brand-name">VELTRA</div>
    <p class="foot-text" style="margin-top:18px;font-size:12px">© Copyright 2014 veltra-example.co.uk<br>All Rights Reserved</p>
  </div>
</footer>

</body>
</html>
```